stationary for hygienic company

We need a stationary design for hygienic company which provides public high end sanitary products and high end public lavatory.
We need a fresh and clean style stationary
we want the following things:
* logo (redesigned in eps/vector)
* Letterhead (with company details)
* letterhead (without company details)
* Business card
* note block
* ballpoint
* etcetera (a complete package)

```html
<!DOCTYPE html>
<html lang="fr">
<head>
<meta charset="utf-8">
<title>Velmira – Business Card</title>
<link href="https://fonts.googleapis.com/css2?family=Didact+Gothic&display=swap" rel="stylesheet">
<style>
  :root {
    --backdrop: #e6e7ea;
    --card: #ffffff;
    --ink: #1c1c22;
    --magenta: #e2127f;
    --navy: #1d1a80;
    --sky: #1aa6e0;
  }
  * { margin: 0; padding: 0; box-sizing: border-box; }
  html, body {
    width: 1200px; height: 901px; overflow: hidden;
    background: var(--backdrop);
    font-family: "Didact Gothic", sans-serif;
    color: var(--ink);
  }
  .business-card {
    position: absolute; left: 100px; top: 165px;
    width: 1000px; height: 570px;
    background: var(--card);
    box-shadow: 0 18px 40px rgba(0,0,0,0.18);
    overflow: hidden;
  }
  .brand {
    position: absolute; left: 70px; top: 150px;
  }
  .brand-mark {
    display: block; width: 70px; height: 70px; border-radius: 50%;
    background: var(--magenta); margin: 0 0 22px 150px;
  }
  .brand-name {
    font-size: 118px; line-height: 1; letter-spacing: -1px;
  }
  .brand-tagline {
    font-size: 34px; margin-top: 6px; padding-left: 40px;
  }
  .brand-trademark {
    font-size: 17px; margin-top: 6px; padding-left: 95px;
  }
  .divider {
    position: absolute; top: 95px; width: 3px; height: 380px;
  }
  .divider--magenta { left: 470px; background: var(--magenta); }
  .divider--sky { left: 480px; background: var(--sky); }
  .contact {
    position: absolute; left: 540px; top: 80px;
  }
  .contact-name { font-size: 34px; }
  .contact-role { font-size: 24px; margin-bottom: 28px; }
  .contact-list { list-style: none; font-size: 22px; line-height: 1.45; padding-left: 30px; }
  .contact-list .label { display: inline-block; width: 90px; }
  .colour-band {
    position: absolute; left: 0; bottom: 0; width: 100%; height: 58px; display: flex;
  }
  .colour-band .magenta { flex: 0 0 52%; background: var(--magenta); }
  .colour-band .navy { flex: 0 0 9%; background: var(--navy); }
  .colour-band .sky { flex: 1; background: var(--sky); }
</style>
</head>
<body>
  <div class="business-card">
    <div class="brand">
      <span class="brand-mark"></span>
      <div class="brand-name">Velmira</div>
      <div class="brand-tagline">Boutique Hygienique</div>
      <div class="brand-trademark">Marque déposée</div>
    </div>

    <div class="divider divider--magenta"></div>
    <div class="divider divider--sky"></div>

    <div class="contact">
      <div class="contact-name">Your Name</div>
      <div class="contact-role">Designation</div>
      <ul class="contact-list">
        <li>Velmira Ltd.</li>
        <li>Address line 1,</li>
        <li>Adressline 2,</li>
        <li>City, Country,</li>
        <li><span class="label">Tel</span>: +00 00 0000000</li>
        <li><span class="label">Fax</span>: +00 00 0000000</li>
        <li><span class="label">E-mail</span>: hello@velmira.com</li>
        <li><span class="label">Web</span>: www.velmira.com</li>
      </ul>
    </div>

    <div class="colour-band">
      <div class="magenta"></div>
      <div class="navy"></div>
      <div class="sky"></div>
    </div>
  </div>
</body>
</html>
```